Redwell - Rebranding, Namecard, Stationary and One Page Web

Refresh logo, make it modern and design matching name card, stationary and one page web

Redwell Information Technology (Int'l) Company Limited
紅井訊息科技(國際)有限公司

Company is System Integrator, and will be providing products and services to government and enterprise organizations. Our Chief Security Officer came from top U.S. vendor, and had been working on top enterprise and government projects globally, so we want the refreshed image of the new company to have a East Cost U.S. style, with hint of technology from Silicon Valley. The company will also be representing top brands from the U.S. on information security.

Branding refresh is needed because company is being acquired and is expanding

Target Market(s)

Cyber Security

Industry/Entity Type

Information Technology

Contact Information for Business Card

Need Chinese and English

Number of Pages Required

1 page

Font styles to use
Sans Serif

Colors
0292cd
00a990

Requirements
Must have
• Modern, clean, cyber look. Must keep same colors and general look and feel of original logo. Only modernization, do not change its personality

```html
<!DOCTYPE html>
<html lang="en">
<head>
<meta charset="utf-8">
<title>Redwell Stationery</title>
<link rel="stylesheet" href="https://fonts.googleapis.com/css2?family=Open+Sans:wght@400;600;700;800&family=Oswald:wght@400;500&family=Tinos&family=Noto+Sans+TC:wght@400&display=swap">
<style>
  :root {
    --blue: #0292cd;
    --blue-card: #1d8fd2;
    --green: #00a990;
    --teal: #2fbfa8;
    --folder-top: #5cc9ea;
    --folder-bottom: #3aaae3;
    --paper: #ffffff;
    --paper-soft: #f2f2f2;
    --bg: #f4f4f4;
    --ink: #444444;
    --grey: #8a8a8a;
  }
  * { box-sizing: border-box; margin: 0; padding: 0; }
  html, body { width: 1200px; height: 1000px; overflow: hidden; }
  body {
    background: var(--bg);
    font-family: "Open Sans", Arial, sans-serif;
    color: var(--ink);
    position: relative;
  }
  .sheet { position: absolute; background: var(--paper); overflow: hidden; }

  .wordmark {
    position: absolute;
    font-family: "Open Sans", Arial, sans-serif;
    font-weight: 800;
    color: var(--blue);
    letter-spacing: 0.5px;
    display: flex;
    align-items: center;
    gap: 6px;
    white-space: nowrap;
  }
  .wordmark .dot { display: inline-block; border-radius: 50%; background: currentColor; }
  .wordmark.light { color: #ffffff; }

  .band { position: absolute; left: 0; right: 0; bottom: 0; display: flex; }
  .band .blue { background: var(--blue); flex: 1; }
  .band .green { background: var(--teal); clip-path: polygon(10px 0, 100% 0, 100% 100%, 0 100%); margin-left: -8px; }

  /* notepad */
  .notepad { left: 47px; top: 130px; width: 165px; height: 240px; background: var(--paper-soft); }
  .notepad .spiral { position: absolute; top: 0; left: 22px; right: 22px; height: 10px;
    border-top: 2px dotted #9a9a9a; }

  /* front card */
  .card-front { left: 16px; top: 407px; width: 283px; height: 161px; background: var(--blue-card); }
  .card-front .company { position: absolute; top: 107px; left: 0; right: 0; text-align: center;
    color: #fff; font-size: 6.5px; line-height: 8.5px; }
  .card-front .company .zh { font-family: "Noto Sans TC", sans-serif; }

  /* back card */
  .card-back { left: 16px; top: 606px; width: 283px; height: 163px; }
  .card-back .tab { position: absolute; left: 0; top: 36px; width: 4px; height: 18px; background: var(--blue); }
  .person-name { position: absolute; left: 15px; top: 34px; font-weight: 700; font-size: 11px; color: var(--blue); letter-spacing: 0.3px; }
  .person-role { position: absolute; left: 15px; top: 50px; font-size: 7px; color: var(--ink); }
  .address { position: absolute; font-size: 6px; line-height: 8.2px; color: var(--ink); }
  .contact-list { position: absolute; list-style: none; font-size: 6.5px; line-height: 10px; color: var(--ink); }
  .contact-list li { display: flex; align-items: center; gap: 5px; }
  .contact-list svg { width: 6px; height: 6px; fill: var(--blue); flex: none; }
  .contact-list .web b { color: var(--blue); font-weight: 400; }

  /* letterhead */
  .letterhead { left: 316px; top: 107px; width: 401px; height: 566px; background: #f7f7f7; }
  .letterhead .addr-block { position: absolute; left: 234px; top: 52px; font-size: 7px; line-height: 9px; color: var(--ink); }
  .letterhead .addr-block p + p { margin-top: 9px; }
  .greeting { position: absolute; left: 20px; top: 178px; font-family: "Oswald", sans-serif; font-weight: 400;
    font-size: 26px; line-height: 28px; color: #8c8c8c; }
  .recipient { position: absolute; left: 20px; top: 209px; font-family: "Oswald", sans-serif; font-weight: 500;
    font-size: 11px; color: #9b9b9b; letter-spacing: 0.3px; }
  .letter-body { position: absolute; left: 20px; top: 238px; width: 362px; font-family: "Tinos", serif;
    font-size: 5.6px; line-height: 7.6px; color: #555; }
  .letter-body p { margin-bottom: 7px; }

  /* folder */
  .folder { left: 741px; top: 74px; width: 377px; height: 600px;
    background: linear-gradient(180deg, var(--folder-top), var(--folder-bottom)); }
  .folder .strap { position: absolute; right: 4px; top: 0; bottom: 0; width: 2px; background: rgba(255,255,255,0.55); }

  /* envelopes */
  .envelope-front { left: 317px; top: 706px; width: 420px; height: 208px; background: #f7f7f7; }
  .envelope-front .divider { position: absolute; left: 157px; top: 143px; width: 1px; height: 24px; background: var(--blue); }
  .envelope-back { left: 755px; top: 703px; width: 410px; height: 208px; background: #f7f7f7; }
  .envelope-back .flap { position: absolute; inset: 0; }
</style>
</head>
<body>

  <!-- Notepad -->
  <div class="sheet notepad">
    <div class="spiral"></div>
    <div class="wordmark" style="left:38px; top:110px; font-size:17px;"><span class="dot" style="width:8px;height:8px;"></span>REDWELL</div>
  </div>

  <!-- Business card front -->
  <div class="sheet card-front">
    <div class="wordmark light" style="left:103px; top:64px; font-size:14px;"><span class="dot" style="width:7px;height:7px;"></span>REDWELL</div>
    <div class="company">
      <p>Redwell Information Technology (Int'l) Company Limited</p>
      <p class="zh">紅井訊息科技(國際)有限公司</p>
    </div>
  </div>

  <!-- Business card back -->
  <div class="sheet card-back">
    <div class="tab"></div>
    <p class="person-name">DANIEL HO</p>
    <p class="person-role">CEO</p>
    <p class="address" style="left:15px; top:76px;">Room B, Unit 402, 4/F, Harbour Tech Bldg,<br>No. 12 Lee Chung Road, Kwun Tong,<br>Kowloon, HKSAR</p>
    <ul class="contact-list" style="left:15px; top:111px;">
      <li><svg viewBox="0 0 10 10"><path d="M2 0h2l1 3-1.5 1a6 6 0 0 0 2.5 2.5L7 5l3 1v2a2 2 0 0 1-2 2A8 8 0 0 1 0 2a2 2 0 0 1 2-2z"/></svg>(852) 5550 1234</li>
      <li><svg viewBox="0 0 10 10"><path d="M0 2h10v6H0z M0 2l5 3.5L10 2" stroke="#fff" stroke-width="0.8"/></svg>danielho@hkredwell.com.hk</li>
      <li class="web"><svg viewBox="0 0 10 10"><circle cx="5" cy="5" r="5"/></svg>www.<b>hkredwell</b>.com.hk</li>
    </ul>
    <div class="wordmark" style="left:188px; top:102px; font-size:14px;"><span class="dot" style="width:7px;height:7px;"></span>REDWELL</div>
    <div class="band" style="height:10px;"><div class="blue"></div><div class="green" style="width:86px;"></div></div>
  </div>

  <!-- Letterhead -->
  <div class="sheet letterhead">
    <div class="wordmark" style="left:20px; top:84px; font-size:22px;"><span class="dot" style="width:10px;height:10px;"></span>REDWELL</div>
    <div class="addr-block">
      <p>Room B, Unit 402, 4/F, Harbour Tech Bldg,<br>No. 12 Lee Chung Road,<br>Kwun Tong, Kowloon, HKSAR</p>
      <p>(852) 5550 1234<br>danielho@hkredwell.com.hk<br>www.hkredwell.com.hk</p>
    </div>
    <h1 class="greeting">HELLO</h1>
    <p class="recipient">MR. LEE</p>
    <div class="letter-body">
      <p>Thank you for meeting with our team last week. We are pleased to share a short summary of the security review and the next steps we agreed on together.</p>
      <p>Our engineers have completed the audit of your network and found that most systems are well protected. A few older servers still need updates, and we suggest moving them to the new firewall plan before the end of the quarter. We will send the full report by email, with clear notes on each item, the risk level and the time needed to fix it. Please let us know if your staff would like a short training session on the new tools.</p>
      <p>We also reviewed the access rules for your remote offices. The current setup works, but a single sign-on system would make daily work easier and safer for every user.</p>
      <p>Our support desk is open every day, and your account manager will call you next Monday to confirm the plan.</p>
      <p>The first phase covers the main office and data centre. Work will take place after hours so that your teams are not disturbed, and each change will be tested before it goes live.</p>
      <p>The second phase adds monitoring for all branch sites. Alerts will reach our team at once, and monthly reports will show trends, threats blocked and areas to improve.</p>
      <p>We look forward to working with you on this project.</p>
      <p>Regards,<br>Alan Wong.<br>02.02.2014</p>
    </div>
    <div class="band" style="height:16px;"><div class="blue"></div><div class="green" style="width:114px;"></div></div>
  </div>

  <!-- Presentation folder -->
  <div class="sheet folder">
    <div class="strap"></div>
    <div class="wordmark light" style="left:70px; top:280px; font-size:38px;"><span class="dot" style="width:18px;height:18px;"></span>REDWELL</div>
  </div>

  <!-- DL envelope front -->
  <div class="sheet envelope-front">
    <div class="wordmark" style="left:23px; top:46px; font-size:17px;"><span class="dot" style="width:8px;height:8px;"></span>REDWELL</div>
    <ul class="contact-list" style="left:23px; top:140px;">
      <li><svg viewBox="0 0 10 10"><path d="M2 0h2l1 3-1.5 1a6 6 0 0 0 2.5 2.5L7 5l3 1v2a2 2 0 0 1-2 2A8 8 0 0 1 0 2a2 2 0 0 1 2-2z"/></svg>(852) 5550 1234</li>
      <li><svg viewBox="0 0 10 10"><path d="M0 2h10v6H0z M0 2l5 3.5L10 2" stroke="#fff" stroke-width="0.8"/></svg>danielho@hkredwell.com.hk</li>
      <li class="web"><svg viewBox="0 0 10 10"><circle cx="5" cy="5" r="5"/></svg>www.<b>hkredwell</b>.com.hk</li>
    </ul>
    <div class="divider"></div>
    <p class="address" style="left:177px; top:142px; font-size:6.5px; line-height:10px;">Room B, Unit 402, 4/F, Harbour Tech Bldg,<br>No. 12 Lee Chung Road, Kwun Tong,<br>Kowloon, HKSAR</p>
    <div class="band" style="height:12px;"><div class="blue"></div><div class="green" style="width:112px;"></div></div>
  </div>

  <!-- DL envelope back -->
  <div class="sheet envelope-back">
    <svg class="flap" viewBox="0 0 410 208" preserveAspectRatio="none" aria-hidden="true">
      <polyline points="0,0 205,58 410,0" fill="none" stroke="#dcdcdc" stroke-width="1.2"/>
    </svg>
    <div class="wordmark" style="left:135px; top:125px; font-size:22px;"><span class="dot" style="width:10px;height:10px;"></span>REDWELL</div>
  </div>

</body>
</html>
```